Zielgruppe
Beamer Vermietung
Aufgabenstellung
Erstellung 2 professionell aussehender Webseiten.
Projektor-Verleih-Region-Wendlar.de
sowie
Projektor-Verleih-Region-Haselfurtheim.de
Die Seiten sind aktuell im Betrieb, aber haben ein sehr veraltetes Design.
Die Seiten können ähnlich aussehen, sollten aber etwas unterschiedlich sein, damit sie für den Kunden leicht anders aussehen.
Wichtig ist, dass alle Seiten, inklusive Startseite, Unterseiten und Links designed werden und das dieses Design in die bestehende Wordpress Installation eingepflegt wird.
Es ist also notwendig, gute Wordpress Kenntnisse zu haben um dann auch zwei fertige Wordpress Seiten liefern zu können.

```html
<!DOCTYPE html>
<html lang="de">
<head>
<meta charset="utf-8">
<title>Projektor-Verleih Haselfurtheim</title>
<link href="https://fonts.googleapis.com/css2?family=Roboto:wght@400;500;700&display=swap" rel="stylesheet">
<style>
:root{
  --orange:#fb5b1e;
  --ink:#222;
  --text:#333;
  --muted:#888;
  --nav:#ebebeb;
  --footer:#ececec;
  --copy:#dcdcdc;
  --white:#fff;
}
*{margin:0;padding:0;box-sizing:border-box}
html,body{width:687px;height:1200px;overflow:hidden;background:var(--white)}
body{position:relative;font-family:'Roboto',sans-serif;color:var(--text)}
.abs{position:absolute}
.brand-name{font-family:'Roboto',sans-serif;font-weight:500;color:var(--ink);font-size:10px;letter-spacing:.2px;white-space:nowrap}
.brand-sub{font-size:5px;color:var(--ink);white-space:nowrap}
.btn{position:absolute;border-radius:8px;font-size:5.4px;font-weight:500;display:flex;align-items:center;justify-content:center;text-transform:uppercase;white-space:nowrap}
.btn-solid{background:var(--orange);color:var(--white)}
.btn-outline{border:1px solid var(--orange);color:var(--orange);background:transparent}
.nav{top:50px;left:0;width:687px;height:21px;background:var(--nav)}
.nav span{position:absolute;top:7.5px;font-size:5.6px;font-weight:500;color:var(--ink)}
.hero{top:71px;left:0;width:687px;height:218px;background:linear-gradient(100deg,#c9ced6 0%,#aeb6c2 30%,#d7dbe2 55%,#e7e9ee 70%,#8d96a5 85%,#cfd4dc 100%)}
.hero-fade{top:71px;left:0;width:687px;height:218px;background:linear-gradient(180deg,rgba(255,255,255,.15),rgba(255,255,255,.35) 70%,rgba(255,255,255,.1))}
.hero-title{top:130px;left:57px;font-size:17px;font-weight:700;color:var(--ink);letter-spacing:-.3px;white-space:nowrap}
.hero-sub{top:149px;left:57px;font-size:9.4px;color:var(--ink);white-space:nowrap}
.hero-cta{top:174px;left:58px;font-size:7px;color:var(--white)}
.hero-phone{top:181px;left:58px;font-size:12.3px;font-weight:700;color:var(--white)}
.eyebrow{width:687px;text-align:center;color:var(--orange);font-size:8.6px}
.section-title{width:687px;text-align:center;color:var(--ink);font-size:10.4px;font-weight:500}
.copy{font-size:5.2px;line-height:8.6px;color:var(--ink)}
.copy p+p{margin-top:8.6px}
.copy .hl{color:var(--orange)}
.copy a{color:var(--orange);text-decoration:underline}
.band{top:454px;left:0;width:687px;height:133px;background:linear-gradient(90deg,#e4e3e1,#d9d6d3 35%,#e2e0dd 60%,#d8d6d4)}
.band-text{top:482px;left:0;width:687px;text-align:center}
.band-text h2{font-size:10.4px;font-weight:500;color:var(--ink)}
.band-text p{font-size:7.4px;line-height:11.5px;font-weight:400;color:var(--text);margin-top:3px}
.product-img{top:661px;width:182px;height:107px}
.product h3{position:absolute;font-size:7.5px;font-weight:400;color:var(--ink);white-space:nowrap}
.product p{position:absolute;font-size:4.9px;line-height:6.8px;color:var(--text);width:182px}
.product a{position:absolute;font-size:5.2px;color:var(--orange);text-decoration:none}
.why-title{top:850px;width:687px;text-align:center;font-size:12.5px;font-weight:500;color:var(--ink)}
.why-sub{top:871px;width:687px;text-align:center;font-size:5.4px;line-height:9px;color:var(--muted)}
.card{top:909px;width:129px;height:95px;background:var(--white);box-shadow:0 1px 5px rgba(0,0,0,.08);text-align:center}
.card svg{position:absolute;left:50%;top:12px;transform:translateX(-50%)}
.card h4{position:absolute;top:48px;width:100%;font-size:7px;font-weight:500;color:var(--ink)}
.card p{position:absolute;top:59px;width:100%;padding:0 10px;font-size:5.3px;line-height:9px;color:var(--muted)}
.footer{top:1052px;left:0;width:687px;height:103px;background:var(--footer)}
.foot-links{top:1066px;left:58px;list-style:none}
.foot-links li{font-size:5.2px;line-height:10.8px;color:var(--ink)}
.foot-links li::before{content:"";display:inline-block;width:2px;height:2px;border-radius:50%;background:var(--ink);margin-right:4px;vertical-align:middle}
.contact{left:218px;font-size:5.2px;line-height:9.3px;color:var(--ink);white-space:nowrap}
.foot-brand{top:1074px;left:418px;width:207px;height:30px;background:#f2f2f2;border:1px solid #e0e0e0;padding:5px 6px}
.social{top:1113px;width:17px;height:17px;border-radius:50%;background:#c9c9c9}
.copyright{top:1155px;left:0;width:687px;height:19px;background:var(--copy);font-size:5.2px;color:var(--ink);text-align:center;line-height:19px}
</style>
</head>
<body>

<header>
  <div class="abs brand-name" style="top:20px;left:57px">PROJEKTOR-VERLEIH HASELFURTHEIM</div>
  <div class="abs brand-sub" style="top:32px;left:57px">Projektor-Verleih-Region-Haselfurtheim.de – Beamer mieten in Haselfurtheim</div>
  <div class="btn btn-solid" style="top:21px;left:449px;width:94px;height:14px">Reservieren oder Buchen</div>
</header>

<nav class="abs nav">
  <span style="left:57px">BEAMER MIETEN</span>
  <span style="left:121px">HD BEAMER MIETEN</span>
  <span style="left:199px">FULL-HD BEAMER MIETEN</span>
  <span style="left:289px">KONTAKT / ANREISE</span>
  <span style="left:366px">PREISLISTE</span>
  <span style="left:418px">DATENSCHUTZERKLÄRUNG</span>
  <span style="left:509px">IMPRESSUM</span>
</nav>

<section>
  <div class="abs hero" role="img" aria-label="Unscharfer Konferenzraum mit großem Projektor im Vordergrund"></div>
  <div class="abs hero-fade"></div>
  <div class="abs hero-title">BEAMER MIETEN ZU TOP-KONDITIONEN</div>
  <div class="abs hero-sub">Sie möchten einen Beamer im Kreis Haselfurtheim oder Umgebung mieten?</div>
  <div class="abs hero-cta">JETZT KONTAKTIEREN</div>
  <div class="abs hero-phone">02741 / 550123</div>
  <svg class="abs" style="top:150px;left:436px" width="74" height="74" viewBox="0 0 74 74">
    <circle cx="39" cy="39" r="33" fill="#3a3a3a" opacity=".85"/>
    <circle cx="36" cy="36" r="33" fill="#fff"/>
    <g transform="rotate(-18 36 36)" font-family="Roboto, sans-serif" text-anchor="middle" fill="#222">
      <text x="36" y="22" font-size="5.8">Projektoren und</text>
      <text x="36" y="28.5" font-size="5.8">Leinwände ab</text>
      <text x="36" y="35" font-size="5.8">bereits</text>
      <text x="31" y="50" font-size="15" font-weight="700" fill="#fb5b1e">30€</text>
      <text x="49" y="53" font-size="4.6" text-anchor="start">pro Tag</text>
    </g>
  </svg>
</section>

<section>
  <div class="abs eyebrow" style="top:316px">WILLKOMMEN ZU</div>
  <div class="abs section-title" style="top:327px">BEAMER VERMIETUNG KREIS HASELFURTHEIM</div>
  <div class="abs copy" style="top:360px;left:57px;width:280px">
    <p>Zu unseren Miet-Geräten können optional auch passende Leinwände zu Ihrem gewünschten Projektor hinzugebucht werden. Unsere Projektoren und Leinwände gibt es bereits ab günstigen <span class="hl">30€ pro Tag</span>. Alle Preise können Sie unserer Preisliste entnehmen.</p>
    <p>Unser Sortiment erstreckt sich von Heim-Projektoren für den privaten Bedarf über HD-fähige Geräte bis hin zu Business Full-HD-Geräten, die für großräumige Geschäftspräsentationen sowie für Full-HD TV Übertragungen geeignet sind. Somit haben Sie das perfekte Klang- und Bilderlebnis für Ihre Präsentation oder Ihr Event.</p>
  </div>
  <div class="abs copy" style="top:360px;left:352px;width:285px">
    <p>Wir bieten Ihnen die Möglichkeit, auch über Wochenenden zu vergünstigten Wochenend-Tarifen zu bestellen. Falls Sie Fragen zu dem Ablauf, zu den Projektoren oder zu dem Mietvorgang haben, können Sie uns jederzeit kontaktieren, wir helfen Ihnen gerne weiter!</p>
    <p>Sie kommen aus dem Kreis Wendlar? Unsere aktuellen Angebote hierfür finden Sie unter<br><a href="#">https://www.projektor-verleih-region-wendlar.de</a></p>
    <p>Bei Fragen zur Anfahrt können Sie unseren Anfahrt-Navigator unter „Kontakt / Anreise“ nutzen.</p>
  </div>
</section>

<section>
  <div class="abs band" role="img" aria-label="Blasses Foto einer jubelnden Gruppe vor einer Leinwand"></div>
  <div class="abs band-text">
    <h2>AUF DER SUCHE NACH DEM PERFEKTEN PROJEKTOR?</h2>
    <p>Wir können Ihnen helfen, einen Projektor zu finden, der auf den von Ihnen<br>benötigten Funktionen basiert.</p>
  </div>
  <div class="btn btn-outline" style="top:537px;left:257px;width:73px;height:14px">Siehe Preisliste</div>
  <div class="btn btn-solid" style="top:537px;left:336px;width:94px;height:14px">Reservieren oder Buchen</div>
</section>

<section>
  <div class="abs eyebrow" style="top:620px;left:10px">UNSER BESTES</div>
  <div class="abs section-title" style="top:632px;left:10px">BEAMER MIETEN</div>

  <div class="product">
    <div class="abs product-img" style="left:57px;background:linear-gradient(160deg,#6d6a66,#3c3a38 60%,#a9a49e)" role="img" aria-label="Schwarzer Projektor auf einem Tisch, dahinter ein Besprechungsraum"></div>
    <h3 style="top:775px;left:56px">Beamer Modell Lumora LX520</h3>
    <p style="top:786px;left:57px">Lorem ipsum dolor sit amet, consectetur adipiscing elit, sed do eiusmod tempor incididunt ut labore et dolore magna aliqua.</p>
    <a href="#" style="top:806px;left:57px">BUCHEN SIE JETZT</a>
  </div>
  <div class="product">
    <div class="abs product-img" style="left:253px;background:linear-gradient(150deg,#3a2a1f,#7a5232 45%,#c9c6c2 80%,#6f90a8)" role="img" aria-label="Weißer Projektor in einem warm beleuchteten Wohnzimmer mit Projektion an der Wand"></div>
    <h3 style="top:775px;left:252px">HD-Beamer Modell Brightvale V710</h3>
    <p style="top:786px;left:253px">Lorem ipsum dolor sit amet, consectetur adipiscing elit, sed do eiusmod tempor incididunt ut labore et dolore magna aliqua.</p>
    <a href="#" style="top:806px;left:253px">BUCHEN SIE JETZT</a>
  </div>
  <div class="product">
    <div class="abs product-img" style="left:448px;background:linear-gradient(160deg,#2f3340,#5c6170 50%,#d6d6d6 80%,#eeeeee)" role="img" aria-label="Weißer Projektor vor Publikum in einem Veranstaltungssaal"></div>
    <h3 style="top:775px;left:448px">Full-HD-Beamer Modell Visiqon HD24-LV</h3>
    <p style="top:786px;left:448px">Lorem ipsum dolor sit amet, consectetur adipiscing elit, sed do eiusmod tempor incididunt ut labore et dolore magna aliqua.</p>
    <a href="#" style="top:806px;left:448px">BUCHEN SIE JETZT</a>
  </div>
</section>

<section>
  <div class="abs why-title" style="left:6px">WARUM UNS WÄHLEN ?</div>
  <div class="abs why-sub">Lorem ipsum dolor sit amet, consectetur adipiscing elit, sed do eiusmod tempor incididunt ut<br>labore et dolore magna aliqua.</div>

  <div class="abs card" style="left:135px">
    <svg width="38" height="24" viewBox="0 0 38 24" fill="none" stroke="#fb5b1e" stroke-width="1.4">
      <rect x="1" y="3" width="36" height="16" rx="3"/>
      <circle cx="11" cy="11" r="6"/><circle cx="11" cy="11" r="3.5"/>
      <line x1="21" y1="8" x2="33" y2="8"/><line x1="21" y1="11" x2="33" y2="11"/><line x1="21" y1="14" x2="33" y2="14"/>
      <line x1="6" y1="19" x2="6" y2="22"/><line x1="32" y1="19" x2="32" y2="22"/>
    </svg>
    <h4>Neueste Ausrüstung</h4>
    <p>Wir verwenden nur die neuesten Technologien.</p>
  </div>
  <div class="abs card" style="left:288px">
    <svg width="30" height="30" viewBox="0 0 30 30" fill="none" stroke="#fb5b1e" stroke-width="1.4">
      <path d="M7 12a8 8 0 0 1 16 0"/>
      <rect x="5" y="11" width="4" height="6" rx="1.5"/><rect x="21" y="11" width="4" height="6" rx="1.5"/>
      <path d="M23 17c0 3-3 4-6 4"/>
      <path d="M3 29v-4a6 6 0 0 1 6-6h12a6 6 0 0 1 6 6v4z"/>
      <rect x="11" y="23" width="8" height="5"/>
    </svg>
    <h4>Erstaunliche Unterstützung</h4>
    <p>Wir garantieren eine schnelle und effektive Antwort auf Ihre Anfragen.</p>
  </div>
  <div class="abs card" style="left:442px">
    <svg width="30" height="30" viewBox="0 0 30 30" fill="none" stroke="#fb5b1e" stroke-width="1.4">
      <circle cx="15" cy="15" r="13.5" stroke-dasharray="3 1.5"/>
      <circle cx="15" cy="15" r="10"/>
      <rect x="9" y="14" width="3" height="6"/>
      <path d="M12 14l3-5c1 0 1.5 1 1.2 2l-.6 2h4c1 0 1.6.8 1.4 1.6l-1 4.4H12"/>
    </svg>
    <h4>Preisgarantie</h4>
    <p>Wir können sicherstellen, dass die Qualität der Ausrüstung vergleichbar ist.</p>
  </div>
</section>

<footer>
  <div class="abs footer"></div>
  <ul class="abs foot-links">
    <li>Beamer mieten</li><li>HD Beamer mieten</li><li>Full-HD Beamer mieten</li><li>Kontakt / Anreise</li><li>Preisliste</li><li>Datenschutzerklärung</li><li>Impressum</li>
  </ul>

  <svg class="abs" style="top:1067px;left:203px" width="10" height="12" viewBox="0 0 10 12" fill="none" stroke="#444" stroke-width=".8">
    <path d="M5 11.5S1 7 1 4.5a4 4 0 0 1 8 0C9 7 5 11.5 5 11.5z"/><circle cx="5" cy="4.5" r="1.5"/>
  </svg>
  <div class="abs contact" style="top:1066px">Kessler Marwin GbR, Lindenweg 7,<br>57199 Obernau.</div>

  <svg class="abs" style="top:1093px;left:203px" width="11" height="11" viewBox="0 0 11 11" fill="none" stroke="#444" stroke-width=".8">
    <path d="M2 1l2 2-1 1.5c.8 1.6 2 2.8 3.5 3.5L8 7l2 2-1.5 1.5C4.5 10 1 6.5.5 2.5z"/>
    <path d="M6 1.5a3.5 3.5 0 0 1 3.5 3.5M6 3a2 2 0 0 1 2 2"/>
  </svg>
  <div class="abs contact" style="top:1092px">02741/550123<br>0151/5550147</div>

  <svg class="abs" style="top:1118px;left:203px" width="12" height="11" viewBox="0 0 12 11" fill="none" stroke="#444" stroke-width=".8">
    <rect x=".5" y="2" width="11" height="8.5"/><path d="M.5 2l5.5 4.5L11.5 2"/><path d="M3 .5h6"/>
  </svg>
  <div class="abs contact" style="top:1120px">info@projektor-verleih-region-haselfurtheim.de</div>

  <div class="abs foot-brand">
    <div class="brand-name">PROJEKTOR-VERLEIH HASELFURTHEIM</div>
    <div class="brand-sub" style="margin-top:2px">Projektor-Verleih-Region-Haselfurtheim.de – Beamer mieten in Haselfurtheim</div>
  </div>

  <div class="abs social" style="left:422px"></div>
  <div class="abs social" style="left:445px"></div>
  <div class="abs social" style="left:467px"></div>
  <div class="abs social" style="left:489px"></div>
  <div class="abs social" style="left:512px"></div>
  <div class="abs social" style="left:534px"></div>

  <div class="abs copyright">Copyright © 2020 Projektor-Verleih-Region-Haselfurtheim.de – Beamer mieten in Haselfurtheim. Alle Rechte vorbehalten.</div>
</footer>

</body>
</html>
```